Brand Design

Seeking complete brand image identity. , We have a new logo and are looking for 1) email signature layout, stationery, business cards, newsletter layout, email template designs (3) and social media page covers for linked in, facebook and twitter. We will want an image that can be used for our website header, on press releases as well as for phone website background.

There will be two forms of letterhead. One with all board member names on it and a standard for generic mailings.
Updates

Correction in project description We are seeking a brand identity package that includes 1) stationery (letterhead envelope, business cars), 2) header and footer for PowerPoint layout, 3) Letterhead (.eps & .doc) Email Signature Footer, newsletter template header/footer that can inserted into a Mailchimp newsletter template, Email template header that can e used for standard email blast alert message, and 3 social media templates for facebook, twitter profile, and linked in profile covers. We also want a brand image that can be inserted into a webinar background and webpage header. The logo IS NOT part of the package request. We have a new logo and we are looking to integrate our new logo into a strong brand identity package. The organization is an African American Chamber of Commerce and so images should include Black business people. Website landing page currently is www.vormetbiz.org

Need extra days to review

Target Market(s)

African American business Community

Font styles to use
Sans Serif

Requirements
Must have
• Having a comprehensive identity brand that can be adapted and pushed across a variety of collateral is important to use. For example for proposals and that we can incorporate into a powerpoint presentation.
Nice to have
• Should be professional a we deal with a lot of corporations
Should not have
• Should not in

```html
<!DOCTYPE html>
<html lang="en">
<head>
<meta charset="utf-8">
<title>Vormet Business Chamber – Stationery Set</title>
<link rel="stylesheet" href="https://fonts.googleapis.com/css2?family=Roboto:wght@400;500;700&family=Oswald:wght@500;600&display=swap">
<style>
:root{
  --bg:#e6e7e9;
  --paper:#ffffff;
  --red:#c0202e;
  --red-dark:#9e1622;
  --green:#1e7a4a;
  --ink:#2b2b2b;
  --muted:#6b6b6b;
  --line:#d9d9d9;
}
*{box-sizing:border-box;margin:0;padding:0}
html,body{width:1200px;height:1007px;overflow:hidden}
body{background:var(--bg);font-family:"Roboto",Arial,sans-serif;color:var(--ink);position:relative}
.item{position:absolute;background:var(--paper);box-shadow:0 2px 6px rgba(0,0,0,.12);overflow:hidden}
.brand{display:flex;align-items:center;gap:5px;font-family:"Roboto",Arial,sans-serif;font-weight:700;color:var(--ink);text-transform:uppercase;line-height:1.1}
.brand .mark{width:10px;height:10px;background:var(--red);flex:none}
.brand.light{color:#fff}
.brand.light .mark{background:#fff}

/* Folder */
.folder{left:82px;top:74px;width:348px;height:444px;background:var(--red);display:flex;align-items:center;justify-content:center}
.folder .brand{font-size:17px;letter-spacing:.5px;gap:9px}
.folder .brand .mark{width:16px;height:16px}

/* Letterhead */
.letterhead{left:500px;top:61px;width:294px;height:415px}
.letterhead .brand{position:absolute;right:16px;top:14px;font-size:8px}
.letterhead .body{position:absolute;left:22px;top:70px;right:22px;font-size:6.4px;line-height:1.55;color:#555}
.letterhead .addr{color:var(--ink);font-size:7px;line-height:1.5}
.letterhead .subject{font-weight:700;color:var(--ink);font-size:7px;margin:8px 0 14px}
.letterhead p{margin-bottom:10px}
.letterhead .foot{position:absolute;left:0;bottom:0;width:100%;height:42px;background:var(--green);color:#fff;font-size:6.8px;line-height:1.5;display:flex;justify-content:space-between;align-items:center;padding:0 16px}
.letterhead .foot .right{text-align:right}

/* Tablet & phone screens */
.screen{display:flex;align-items:center;justify-content:center}
.tablet{left:874px;top:89px;width:235px;height:310px}
.tablet .brand{font-size:8.5px}
.phone{left:870px;top:458px;width:90px;height:192px;border-radius:8px}
.phone .brand{font-size:5px;gap:3px}
.phone .brand .mark{width:6px;height:6px}

/* Small card */
.small-card{left:997px;top:490px;width:154px;height:152px}
.small-card .brand{position:absolute;left:42px;top:50px;font-size:5.5px;gap:3px}
.small-card .brand .mark{width:7px;height:7px}
.small-card .info{position:absolute;left:14px;bottom:22px;right:14px;display:flex;justify-content:space-between;font-size:4.2px;color:#555;line-height:1.4}
.small-card .info strong{display:block;font-size:4.6px;color:var(--ink);margin-bottom:3px}

/* Business cards */
.card-front{left:13px;top:547px;width:208px;height:119px}
.card-front .brand{position:absolute;left:30px;top:42px;font-size:7.5px}
.card-front .url{position:absolute;left:0;width:100%;top:78px;text-align:center;color:var(--red);font-size:10.5px;letter-spacing:.3px}
.card-back{left:257px;top:551px;width:209px;height:119px}
.card-back .name{position:absolute;left:18px;top:52px;text-align:center;font-size:8.5px;font-weight:700}
.card-back .name span{display:block;font-weight:400;font-size:7.5px}
.card-back .contact{position:absolute;right:12px;top:30px;text-align:right;font-size:8px;line-height:1.6}
.card-back .contact b{font-weight:700}

/* Envelope */
.envelope{left:500px;top:528px;width:308px;height:144px}
.envelope svg{position:absolute;left:0;top:0}
.envelope .brand{position:absolute;right:14px;top:84px;font-size:7.5px}
.envelope .addr{position:absolute;right:14px;bottom:8px;text-align:right;font-size:7.2px;line-height:1.6}
.envelope .addr b{font-weight:700}

/* Slides */
.slide{width:340px;height:192px;top:730px}
.slide-cover{left:13px}
.slide-cover .brand{position:absolute;left:184px;top:64px;font-size:8.5px}
.slide-cover .title{position:absolute;left:208px;top:112px;font-size:17px;color:var(--red)}
.slide-cover .subtitle{position:absolute;left:268px;top:132px;font-size:12px;color:var(--green)}

.slide-about{left:415px}
.slide-about .photo{position:absolute;left:0;top:0;width:166px;height:192px;background:linear-gradient(135deg,#b51d2a,#8a1420 70%,#a31a27)}
.slide-about .photo p{position:absolute;left:18px;top:78px;right:14px;font-size:5.8px;font-style:italic;color:#fff;line-height:1.5}
.slide-about h2{position:absolute;left:183px;top:14px;font-family:"Oswald",Arial,sans-serif;font-weight:600;font-size:16px}
.slide-about .rule{position:absolute;left:183px;top:40px;width:14px;height:2px;background:var(--red)}
.slide-about .text{position:absolute;left:183px;top:50px;right:18px;font-size:3.8px;line-height:1.55;color:#666}
.slide-about .text p{margin-bottom:6px}
.slide-about .points{position:absolute;left:183px;top:120px;right:18px;font-size:3.8px;color:#666}
.slide-about .point{display:flex;gap:5px;margin-bottom:10px}
.slide-about .point i{width:9px;height:9px;border-radius:50%;background:var(--green);flex:none}
.slide-about .point b{display:block;color:var(--ink);font-size:4.2px}
.corner-tag{position:absolute;right:0;bottom:0;width:46px;height:12px;clip-path:polygon(10px 0,100% 0,100% 100%,0 100%);color:#fff;font-size:4.5px;display:flex;align-items:center;justify-content:flex-end;padding-right:8px}
.slide-about .corner-tag{background:var(--red)}
.square-tag{position:absolute;right:8px;top:6px;width:10px;height:10px;background:var(--red)}

.slide-features{left:822px}
.slide-features .band{position:absolute;left:0;top:0;width:318px;height:20px;background:var(--red);color:#fff;font-family:"Oswald",Arial,sans-serif;font-weight:500;font-size:10.5px;padding:3px 8px}
.slide-features .cols{position:absolute;left:21px;top:69px;width:298px;height:80px;display:flex}
.slide-features .col{flex:1;color:#fff;text-align:center;padding:8px 6px 0;font-size:3.6px;line-height:1.5}
.slide-features .col:nth-child(odd){background:var(--green)}
.slide-features .col:nth-child(even){background:var(--red)}
.slide-features .col .ic{width:10px;height:10px;border-radius:50%;background:rgba(255,255,255,.25);margin:0 auto 6px;display:flex;align-items:center;justify-content:center}
.slide-features .col b{display:block;font-size:4.4px;margin-bottom:3px}
.slide-features .base{position:absolute;left:0;bottom:0;width:100%;height:3px;background:var(--red)}
.slide-features .corner-tag{background:var(--green)}
</style>
</head>
<body>

<section class="item folder" aria-label="Presentation folder">
  <div class="brand light"><span class="mark"></span>Vormet Business Chamber</div>
</section>

<section class="item letterhead" aria-label="Letterhead">
  <div class="brand"><span class="mark"></span>Vormet Business Chamber</div>
  <div class="body">
    <div class="addr">123 Street Hal,<br>California 5640, USA</div>
    <div class="subject">Subject : Loram ispum dolor sit amet.</div>
    <p>Lorem ipsum dolor sit amet, condecteur adipiscing edit. Aenean eros ut cursus cursus. In rhoncus, lacus id Lorem ispum dolor sit amet, condecteur adipiscing edit. Aenean eros ut cursus cursus. In rhoncus, lacus id Loram ispum dolor sit amet, condecteur adipiscing edit. Aenean eros ut cursus cursus. In rhoncus, lacus id Loram ispum dolor sit amet, condecteur adipiscing edit. Aenean eros ut cursus cursus. In rhoncus, lacus id Loram ispum dolor sit amet, condecteur adipiscing edit.</p>
    <p>Aenean eros ut cursus cursus. In rhoncus, lacus id Loram ispum dolor sit amet, condecteur adipiscing edit. Aenean eros ut cursus cursus. In rhoncus, lacus id Loram ispum dolor sit amet, condecteur adipiscing edit. Aenean eros ut cursus cursus. In rhoncus, lacus id Loram ispum dolor sit amet, condecteur adipiscing edit.</p>
    <p>Aenean eros ut cursus cursus. In rhoncus, lacus id Loram ispum dolor sit amet, condecteur adipiscing edit. Aenean eros ut cursus cursus. In rhoncus, lacus id Loram ispum dolor sit amet, condecteur adipiscing edit. Aenean eros ut cursus cursus. In rhoncus, lacus id Loram ispum dolor sit amet, condecteur adipiscing edit. Aenean eros ut cursus cursus. In rhoncus, lacus id Loram ispum dolor sit amet, condecteur adipiscing edit.</p>
  </div>
  <div class="foot">
    <div>123 Street Hal,<br>California 5640, USA</div>
    <div class="right">mail@brandname.com<br>www.brandname.com</div>
  </div>
</section>

<section class="item screen tablet" aria-label="Tablet screen">
  <div class="brand"><span class="mark"></span>Vormet Business Chamber</div>
</section>

<section class="item screen phone" aria-label="Phone screen">
  <div class="brand"><span class="mark"></span>Vormet Business Chamber</div>
</section>

<section class="item small-card" aria-label="Compliment card">
  <div class="brand"><span class="mark"></span>Vormet Business Chamber</div>
  <div class="info">
    <div><strong>COMPANY NAME</strong>123 Street Hal<br>California 5640, USA</div>
    <div>mail@brandname.com<br>www.brandname.com</div>
  </div>
</section>

<section class="item card-front" aria-label="Business card front">
  <div class="brand"><span class="mark"></span>Vormet Business Chamber</div>
  <div class="url">www.brandname.com</div>
</section>

<section class="item card-back" aria-label="Business card back">
  <div class="name">Director Name<span>Designation</span></div>
  <div class="contact">
    123 Street Hal,<br>California 5640, USA<br>
    <b>Phone:</b> 01 1234 654<br>
    <b>Email:</b> mail@brandname.com<br>
    www.brandname.com
  </div>
</section>

<section class="item envelope" aria-label="Envelope">
  <svg width="308" height="144" viewBox="0 0 308 144">
    <polyline points="0,0 154,50 308,0" fill="none" stroke="var(--line)" stroke-width="1"/>
  </svg>
  <div class="brand"><span class="mark"></span>Vormet Business Chamber</div>
  <div class="addr">123 Street Hal, California 5640, USA<br><b>Phone:</b> 01 1234 654 mail@brandname.com • www.brandname.com</div>
</section>

<section class="item slide slide-cover" aria-label="Presentation cover slide">
  <div class="brand"><span class="mark"></span>Vormet Business Chamber</div>
  <div class="title">Project Title here</div>
  <div class="subtitle">Subtext here</div>
</section>

<section class="item slide slide-about" aria-label="About us slide">
  <div class="photo" role="img" aria-label="Photo of Black business professionals in a red duotone">
    <p>Lorem ipsum dolor sit amet, consectetur adipiscing elit, sed do eiusmod tempor incididunt ut labore et dolore magna aliqua.</p>
  </div>
  <span class="square-tag"></span>
  <h2>About Us</h2>
  <span class="rule"></span>
  <div class="text">
    <p>Lorem ipsum dolor sit amet, consectetur adipiscing elit, sed do eiusmod tempor incididunt ut labore et dolore magna aliqua quis nostrud.</p>
    <p>Lorem ipsum dolor sit amet, consectetur adipiscing elit, sed do eiusmod tempor incididunt ut labore et dolore magna aliqua quis nostrud.</p>
  </div>
  <div class="points">
    <div class="point"><i></i><div><b>Your Awesome Title One</b>Lorem ipsum dolor sit amet consectetur elit.</div></div>
    <div class="point"><i></i><div><b>Your Awesome Title Two</b>Lorem ipsum dolor sit amet consectetur elit.</div></div>
  </div>
  <div class="corner-tag">02</div>
</section>

<section class="item slide slide-features" aria-label="Features slide">
  <div class="band">Creative Features</div>
  <span class="square-tag"></span>
  <div class="cols">
    <div class="col"><div class="ic"><svg width="6" height="6" viewBox="0 0 6 6"><path d="M0 3 6 0 4 6 3 3.5Z" fill="#fff"/></svg></div><b>Your Headline One</b>Lorem ipsum dolor sit amet, consectetur elit sed do tempor.</div>
    <div class="col"><div class="ic"><svg width="6" height="6" viewBox="0 0 6 6"><rect x="0" y="1" width="6" height="4" fill="#fff"/></svg></div><b>Your Headline Two</b>Lorem ipsum dolor sit amet, consectetur elit sed do tempor.</div>
    <div class="col"><div class="ic"><svg width="6" height="6" viewBox="0 0 6 6"><path d="M3 0a2 2 0 0 1 2 2c0 1.5-2 4-2 4S1 3.5 1 2a2 2 0 0 1 2-2Z" fill="#fff"/></svg></div><b>Your Headline Three</b>Lorem ipsum dolor sit amet, consectetur elit sed do tempor.</div>
    <div class="col"><div class="ic"><svg width="6" height="6" viewBox="0 0 6 6"><path d="M1 5h4a1.5 1.5 0 0 0 0-3 2 2 0 0 0-4 1 1 1 0 0 0 0 2Z" fill="#fff"/></svg></div><b>Your Headline Four</b>Lorem ipsum dolor sit amet, consectetur elit sed do tempor.</div>
  </div>
  <div class="base"></div>
  <div class="corner-tag">03</div>
</section>

</body>
</html>
```